I need a SEO-friendly Wordpress website (making sure to style H1, H2, H3, etc correctly) for a Hawaii-based law firm called Meridian Crest Legal Group. Comparable websites include https://trvlaw.example/ and https://www.boultem.example/ for design reference. The current copy on the WelbyCounsel.example website can be used.

Coding

```html
<!DOCTYPE html>
<html lang="en">
<head>
<meta charset="utf-8">
<title>Meridian Crest Legal Group</title>
<link rel="stylesheet" href="https://fonts.googleapis.com/css2?family=Montserrat:wght@400;500;600;700;800&family=Raleway:wght@400;500&family=Playfair+Display:wght@700&display=swap">
<style>
:root{
  --brand:#b1600f;
  --brand-dark:#8a3d0b;
  --amber:#e0952f;
  --gold:#d9a06a;
  --footer:#9d4f1c;
  --text:#8a8a8a;
  --light:#f7f7f7;
  --white:#fff;
}
*{margin:0;padding:0;box-sizing:border-box}
html,body{width:1200px;height:3073px;overflow:hidden}
body{position:relative;font-family:"Raleway",sans-serif;background:var(--white);color:var(--text)}
a{color:inherit;text-decoration:none}
.abs{position:absolute}

/* header */
.topbar{left:0;top:0;width:1200px;height:43px;background:var(--brand);border-bottom:1px solid rgba(255,255,255,.2)}
.topbar .item{position:absolute;top:0;height:43px;display:flex;align-items:center;gap:12px;color:#fff;font-family:"Montserrat",sans-serif;font-size:14px;padding:0 20px;border-left:1px solid rgba(255,255,255,.25)}
.topbar .phone{left:673px}
.topbar .mail{left:867px;border-right:1px solid rgba(255,255,255,.25);width:256px}
.nav{left:0;top:43px;width:1200px;height:81px;background:var(--brand)}
.logo{font-family:"Playfair Display",serif;font-weight:700;color:#fff;font-size:38px;position:absolute;left:79px;top:14px}
.menu{position:absolute;left:580px;top:29px;display:flex;gap:38px;font-family:"Montserrat",sans-serif;font-size:16px;color:#fff}
.menu .active{font-weight:600;position:relative}
.menu .active::after{content:"";position:absolute;left:50%;margin-left:-5px;top:26px;border:5px solid transparent;border-bottom:8px solid #fff;border-top:0}
.search{position:absolute;left:1102px;top:30px}

/* hero */
.hero{left:0;top:124px;width:1200px;height:626px}
.hero h1{position:absolute;left:0;top:220px;width:1200px;text-align:center;font-family:"Montserrat",sans-serif;font-weight:800;font-size:50px;line-height:53px;color:var(--brand-dark)}
.arrow{position:absolute;width:62px;height:62px;border-radius:50%;top:240px;display:flex;align-items:center;justify-content:center}
.arrow.prev{left:45px;background:#8a2e0d}
.arrow.next{left:1091px;background:var(--brand)}

/* about */
.about-kicker{left:79px;top:808px;font-family:"Montserrat",sans-serif;font-weight:700;font-size:43px;color:var(--amber)}
.about-title{left:79px;top:860px;font-family:"Montserrat",sans-serif;font-weight:700;font-size:44px;color:var(--brand-dark)}
.about-text{left:79px;top:922px;width:615px;font-size:14px;line-height:26px;color:var(--text)}
.btn{left:78px;top:1136px;width:135px;height:51px;background:var(--brand);color:#fff;font-family:"Montserrat",sans-serif;font-size:16px;display:flex;align-items:center;justify-content:center}
.portrait-ring{left:757px;top:816px;width:367px;height:367px;border-radius:50%;background:var(--amber)}
.portrait{left:748px;top:811px;width:366px;height:366px;border-radius:50%;background:radial-gradient(circle at 50% 40%,#c9a48c 0%,#6c5a54 35%,#1c2a4a 70%,#31452e 100%)}

/* practice */
.practice{left:0;top:1250px;width:1200px;height:614px;background:linear-gradient(180deg,#a5521a 0%,#8f4617 60%,#7e3c13 100%)}
.practice h2{position:absolute;top:56px;width:1200px;text-align:center;font-family:"Montserrat",sans-serif;font-weight:700;font-size:43px;color:#fff}
.card{position:absolute;width:511px;height:188px;background:#fff}
.card .thumb{position:absolute;left:11px;top:11px;width:239px;height:166px}
.card h3{position:absolute;left:267px;top:12px;font-family:"Montserrat",sans-serif;font-weight:500;font-size:23px;color:var(--brand-dark)}
.card p{position:absolute;left:267px;top:52px;width:225px;font-size:14px;line-height:23px;color:var(--text)}
.card .more{position:absolute;left:267px;top:150px;font-family:"Montserrat",sans-serif;font-size:14px;color:var(--amber);text-decoration:underline}

/* strap */
.strap{left:0;top:1923px;width:1200px;text-align:center}
.strap h2{font-family:"Montserrat",sans-serif;font-weight:700;font-size:27px;color:var(--brand)}
.strap p{margin-top:10px;font-size:18px;color:var(--text)}

/* articles */
.articles{left:0;top:2040px;width:1200px;height:360px;background:var(--light)}
.articles .thumb{position:absolute;left:78px;top:64px;width:332px;height:218px}
.articles h2{position:absolute;left:450px;top:60px;font-family:"Montserrat",sans-serif;font-weight:700;font-size:44px;color:var(--brand-dark)}
.articles h3{position:absolute;left:450px;top:126px;font-family:"Montserrat",sans-serif;font-weight:500;font-size:23px;color:var(--amber)}
.articles p{position:absolute;left:450px;top:168px;width:670px;font-size:14px;line-height:26px;color:var(--text)}
.articles .more{position:absolute;left:450px;top:262px;font-family:"Montserrat",sans-serif;font-size:14px;color:var(--amber);text-decoration:underline}
.chev{position:absolute;top:148px}

/* footer */
.footer{left:0;top:2396px;width:1200px;height:677px}
.footer-logo{position:absolute;top:92px;width:1200px;text-align:center;font-family:"Playfair Display",serif;font-weight:700;font-size:40px;color:#fff}
.footer-menu{position:absolute;top:155px;width:1200px;display:flex;justify-content:center;gap:22px;font-family:"Montserrat",sans-serif;font-size:16px;color:#fff}
.footer-rule{position:absolute;left:78px;top:208px;width:1045px;height:1px;background:rgba(255,255,255,.25)}
.col-head{position:absolute;top:260px;font-family:"Montserrat",sans-serif;font-weight:700;font-size:21px;color:var(--amber)}
.links{position:absolute;left:79px;top:312px;list-style:none;font-size:14px;color:#fff}
.links li{height:31px;display:flex;align-items:center;gap:14px}
.links li::before{content:"";width:6px;height:6px;border:1px solid #fff}
.contact{position:absolute;left:274px;top:312px;font-size:14px;color:#fff;line-height:26px}
.contact .row{position:absolute;left:0;display:flex;gap:18px;width:240px}
.contact svg{flex:none;margin-top:4px}
.map{position:absolute;left:531px;top:313px;width:291px;height:197px;background:linear-gradient(135deg,#f4f1ea,#e8e4dc);border:1px solid #ddd}
.social{position:absolute;left:882px;top:312px;list-style:none;color:#fff;font-size:14px}
.social li{height:52px;display:flex;align-items:center;gap:14px}
.social li::before{content:"";width:41px;height:41px;border-radius:50%;background:#fff}
.copy-rule{position:absolute;left:0;top:572px;width:1200px;height:1px;background:rgba(255,255,255,.2)}
.copy{position:absolute;top:614px;width:1200px;text-align:center;font-size:14px;color:#fff}
</style>
</head>
<body>

<header>
  <div class="abs topbar">
    <div class="item phone">
      <svg width="22" height="22" viewBox="0 0 24 24" fill="none" stroke="#fff" stroke-width="1.5"><path d="M5 3h4l2 5-3 2a12 12 0 006 6l2-3 5 2v4a2 2 0 01-2 2A18 18 0 013 5a2 2 0 012-2z"/></svg>
      +1.808.555.0142</div>
    <div class="item mail">
      <svg width="22" height="16" viewBox="0 0 22 16" fill="none" stroke="#fff" stroke-width="1.5"><rect x="1" y="1" width="20" height="14"/><path d="M1 1l10 8 10-8"/></svg>
      clients@welbycounsel.example</div>
  </div>
  <nav class="abs nav">
    <a class="logo" href="#">Meridian Crest Legal Group</a>
    <div class="menu">
      <a class="active" href="#">Home</a><a href="#">Practice Areas</a><a href="#">Attorneys</a><a href="#">Blog</a><a href="#">Contact Us</a>
    </div>
    <svg class="search" width="22" height="22" viewBox="0 0 22 22" fill="none" stroke="#fff" stroke-width="2"><circle cx="9" cy="9" r="7"/><path d="M14 14l6 6"/></svg>
  </nav>
</header>

<section class="abs hero">
  <svg width="1200" height="626" viewBox="0 0 1200 626" style="position:absolute;left:0;top:0">
    <defs>
      <linearGradient id="heroFill" x1="0" y1="0" x2="1" y2="1">
        <stop offset="0" stop-color="#9a8b80"/><stop offset=".45" stop-color="#e9d3bb"/><stop offset="1" stop-color="#7f7570"/>
      </linearGradient>
    </defs>
    <path d="M0 0H1200V501L600 626 0 501Z" fill="#8a3d0b"/>
    <path d="M0 0H1200V501L600 612 0 501Z" fill="url(#heroFill)" role="img" aria-label="Photo of lawyers at a desk with a gavel and documents"/>
    <rect x="423" y="255" width="354" height="334" fill="none" stroke="#d9a06a" stroke-width="20" opacity=".9"/>
  </svg>
  <h1>Dedicated to making sure<br>you receive the care and<br>attention you need</h1>
  <a class="arrow prev" href="#"><svg width="12" height="16" viewBox="0 0 12 16" fill="none" stroke="#fff" stroke-width="2.5"><path d="M9 2L3 8l6 6"/></svg></a>
  <a class="arrow next" href="#"><svg width="12" height="16" viewBox="0 0 12 16" fill="none" stroke="#fff" stroke-width="2.5"><path d="M3 2l6 6-6 6"/></svg></a>
</section>

<section>
  <h2 class="abs about-kicker">About</h2>
  <h2 class="abs about-title">Meridian Crest Legal Group</h2>
  <p class="abs about-text">The experienced attorneys in the Meridian Crest Legal Group's Kailua Kona, Hawaii office provide clients with a wide range of litigation expertise, including legal claims involving divorce &amp; family, personal injury, toxic exposures, intellectual property, and real estate.Our Kona office also offers commercial and hospitality litigation expertise on behalf of a wide variety of clients, including restaurants, hotels, property owners, and many others. We never wish to see our clients go to court, though if there is no other option, you're in safe hands with our seasoned trial lawyers and the many years of courtroom experience behind them.</p>
  <a class="abs btn" href="#">READ MORE</a>
  <div class="abs portrait-ring"></div>
  <div class="abs portrait" role="img" aria-label="Portrait photo of the firm's lead attorney"></div>
</section>

<section class="abs practice">
  <h2>Practice Areas</h2>
  <article class="card" style="left:78px;top:146px">
    <div class="thumb" role="img" aria-label="Photo of a couple reviewing divorce papers" style="background:linear-gradient(135deg,#e6ddd3,#a78e78)"></div>
    <h3>Family &amp; Divorce</h3>
    <p>Our lawyers handle all aspects of family law on the Big Island and neighboring islands. We have more than 70 years.</p>
    <a class="more" href="#">READ MORE</a>
  </article>
  <article class="card" style="left:612px;top:146px">
    <div class="thumb" role="img" aria-label="Photo of a doctor examining an injured patient" style="background:linear-gradient(135deg,#d8dee4,#5e6f84)"></div>
    <h3>Personal Injury</h3>
    <p>Dealing with personal injury and wrongful death claims is hard enough, so the lawyers of MCLG are here to make things.</p>
    <a class="more" href="#">READ MORE</a>
  </article>
  <article class="card" style="left:78px;top:358px">
    <div class="thumb" role="img" aria-label="Photo of a business team meeting" style="background:linear-gradient(135deg,#eef0f2,#4f6a7a)"></div>
    <h3>Corporate &amp; IP</h3>
    <p>The attorneys at MCLG have been helping Big Island business own ers with all their legal needs, so they can stay focused.</p>
    <a class="more" href="#">READ MORE</a>
  </article>
  <article class="card" style="left:612px;top:358px">
    <div class="thumb" role="img" aria-label="Photo of a city skyline reflected in water" style="background:linear-gradient(180deg,#c9a6a0,#7b6f78 55%,#3f4450)"></div>
    <h3>Real Estate</h3>
    <p>Our lawyers work with home own ers, buyers and property develo- pers to ensure timely handling of all legal aspects.</p>
    <a class="more" href="#">READ MORE</a>
  </article>
</section>

<section class="abs strap">
  <h2>Over 70 years of combined practice, specializing in</h2>
  <p>Personal Injury, Family &amp; Divorce, Child Custody</p>
</section>

<section class="abs articles">
  <svg class="chev" style="left:44px" width="18" height="54" viewBox="0 0 18 54" fill="none" stroke="#333" stroke-width="1.5"><path d="M16 1L2 27l14 26"/></svg>
  <div class="thumb" role="img" aria-label="Photo of a lawyer meeting with a couple" style="background:linear-gradient(135deg,#d9d2c8,#6d5a4c)"></div>
  <h2>Articals</h2>
  <h3>Top 10 Things to Do Before Filing for Divorce</h3>
  <p>No one gets married with the intention of things not working out, but it's an unfortunate fact that many marriages don't work out in the end.&nbsp; For those who are in troubled marriage, here are the Top 10 things you should do before filing for a divorce</p>
  <a class="more" href="#">READ MORE</a>
  <svg class="chev" style="left:1138px" width="18" height="54" viewBox="0 0 18 54" fill="none" stroke="#333" stroke-width="1.5"><path d="M2 1l14 26L2 53"/></svg>
</section>

<footer class="abs footer">
  <svg width="1200" height="677" viewBox="0 0 1200 677" style="position:absolute;left:0;top:0">
    <defs>
      <linearGradient id="footFill" x1="0" y1="0" x2="0" y2="1">
        <stop offset="0" stop-color="#b0642a"/><stop offset="1" stop-color="#93481c"/>
      </linearGradient>
    </defs>
    <path d="M0 121L600 0 1200 121V677H0Z" fill="#e0952f"/>
    <path d="M0 121L600 22 1200 121V677H0Z" fill="url(#footFill)" role="img" aria-label="Faded photo of a city skyline"/>
  </svg>
  <div class="footer-logo">Meridian Crest Legal Group</div>
  <div class="footer-menu"><a href="#">Home</a><span>|</span><a href="#">Practice Areas</a><span>|</span><a href="#">Attorneys</a><span>|</span><a href="#">Blog</a><span>|</span><a href="#">Contact Us</a></div>
  <div class="footer-rule"></div>

  <h4 class="col-head" style="left:79px">Practice Areas</h4>
  <ul class="links"><li>Family &amp; Divorce</li><li>Corporate &amp; IP</li><li>Real Estate</li><li>Personal Injury</li></ul>

  <h4 class="col-head" style="left:274px">Get In Touch</h4>
  <div class="contact">
    <div class="row" style="top:0"><svg width="18" height="22" viewBox="0 0 18 22" fill="none" stroke="#e0952f" stroke-width="2"><path d="M9 21s7-7 7-12A7 7 0 002 9c0 5 7 12 7 12z"/><circle cx="9" cy="9" r="2.5"/></svg><span>44-120 Hale Makai Road, Suite 210 Kailua Kona, Hawaii 96740</span></div>
    <div class="row" style="top:94px"><svg width="20" height="20" viewBox="0 0 24 24" fill="#e0952f"><path d="M5 3h4l2 5-3 2a12 12 0 006 6l2-3 5 2v4a2 2 0 01-2 2A18 18 0 013 5a2 2 0 012-2z"/></svg><span>+1.808.555.0142</span></div>
    <div class="row" style="top:141px"><svg width="22" height="16" viewBox="0 0 22 16" fill="none" stroke="#e0952f" stroke-width="2"><rect x="1" y="1" width="20" height="14"/><path d="M1 1l10 8 10-8"/></svg><span>clients@welbycounsel.example</span></div>
  </div>

  <h4 class="col-head" style="left:533px">Location Map</h4>
  <div class="map" role="img" aria-label="Street map showing the office location"></div>

  <h4 class="col-head" style="left:885px">Social Media</h4>
  <ul class="social"><li>Friendpage</li><li>Chirpline</li><li>Worknet</li><li>Searchly</li></ul>

  <div class="copy-rule"></div>
  <p class="copy">Copyright © Meridian Crest Legal Group. All Rights Reserved.</p>
</footer>

</body>
</html>
```